Modern e-Commerce Website for new tea company

We need a web design for a new company called "leaf hollow" based in the UK. We are operating in the food / retailing industry. We are an online retailer of organic Darjeeling Tea (Black and Green Tea) - our clients are end-customers within the UK.

We are looking for a coded wordpress webdesign for a landing page, a potential second page and an online shop.

Target Market(s)

End-customers of tea within the UK

Industry/Entity Type

E-Commerce

Coding

Coded - Design and coding required

Number of Pages Required

3 page

Font styles to use
Other font styles liked:
• Helvetica Neue

Requirements
Must have
• Design expectations:
• We are looking for a very professional looking website. A website that shows the type quality we put into preparing our tea every day. Overall theme of the website should be simplie and clean (white, green). But pictures of tea should be more colourful. Graphics like buttons, text, etc. should be simple, shouldn't stick out too much. Also, don't forget that this website is for people buying tea, so the design should make tea look more appetising.
• Websites that inspire us are:
• https://www.brovanley.co.uk/about-brovanley/brovanley-teas/darjeeling
• - nice colours, icons, graphics
• https://www.plumbrid.com/
• - well designed, simple
• https://www.kelvo.com/
• - simple, clear sections for each point
• How we want each page to be designed
• 1) Landing Page (one-page)
• - sticky menu (header)
• - section 1: slider with pictures of our products
• - section 2: product overview with product pictures
• - section 3: advantages of our products
• - section 4: how our concept works
• - contact us
• - footer (twitter, fb, instagram, disclaimer)
• 2) Second page
• 3) Shop
• Our current site is: http://marpon.sitebox.pw/wp/
Nice to have
• What to avoid
• We want this website to consist of soft colours, so we DON'T want colours that are too hard on the eyes and are "highlighter" like colours. We don't want this website to look too "cartoon like" or too "childish". We are going for a sophisticated, high class look.

```html
<!DOCTYPE html>
<html lang="en">
<head>
<meta charset="utf-8">
<title>Leaf Hollow – Organic Darjeeling Tea</title>
<link rel="stylesheet" href="https://fonts.googleapis.com/css2?family=Raleway:wght@400;600;700;800&family=Open+Sans:wght@400;600;700&display=swap">
<style>
:root{
  --teal:#2f8a8c;
  --teal-dark:#1f6f73;
  --teal-light:#4aa3a0;
  --ink:#222326;
  --text:#555a5e;
  --muted:#8a8f93;
  --line:#dfe3e4;
  --price:#c8423b;
  --gold:#c9a45a;
  --footer:#2d2e32;
  --footer-text:#a9abb0;
  --white:#ffffff;
}
*{margin:0;padding:0;box-sizing:border-box}
html,body{width:1200px;height:4091px;overflow:hidden;background:var(--white)}
body{font-family:"Open Sans",Arial,sans-serif;color:var(--text);position:relative}
h1,h2,h3,h4,.nav,.btn{font-family:"Raleway",Arial,sans-serif}
.btn{display:inline-block;background:var(--teal);color:var(--white);font-weight:700;font-size:14px;letter-spacing:1px;text-transform:uppercase;padding:16px 34px;border-radius:3px}

/* header */
.header{position:absolute;top:0;left:0;width:1200px;height:140px;background:var(--white)}
.brand{position:absolute;left:80px;top:18px;display:flex;flex-direction:column;align-items:center;gap:8px}
.brand-dot{width:72px;height:72px;border-radius:50%;background:var(--ink)}
.brand-name{font-family:"Raleway",sans-serif;font-weight:700;font-size:13px;letter-spacing:1.5px;color:var(--ink);text-transform:uppercase}
.utility{position:absolute;right:80px;top:40px;display:flex;align-items:center;gap:34px;font-size:11px;font-weight:600;text-transform:uppercase;color:var(--ink);letter-spacing:.5px}
.cart{display:flex;align-items:center;gap:10px}
.cart-icon{width:32px;height:32px;border-radius:50%;background:var(--teal);display:flex;align-items:center;justify-content:center}
.nav{position:absolute;right:80px;top:104px;display:flex;gap:46px;font-size:13px;font-weight:700;color:var(--ink);letter-spacing:.8px;text-transform:uppercase}

/* hero */
.hero{position:absolute;top:140px;left:0;width:1200px;height:525px;background:linear-gradient(135deg,#3f5a2a 0%,#6b7a3a 30%,#2a2a22 55%,#8a5a20 75%,#c99a4a 100%);text-align:center;color:var(--white)}
.hero h1{margin-top:185px;font-size:52px;font-weight:700;letter-spacing:6px}
.hero p{margin-top:12px;font-family:"Raleway",sans-serif;font-size:24px;font-weight:600;letter-spacing:3px;text-transform:uppercase}
.hero .btn-outline{display:inline-block;margin-top:26px;border:2px solid var(--white);color:var(--white);font-family:"Raleway",sans-serif;font-weight:700;font-size:13px;letter-spacing:1.5px;padding:10px 26px;text-transform:uppercase}
.scroll-down{position:absolute;left:572px;bottom:-28px;width:56px;height:56px;border-radius:50%;background:var(--white);display:flex;align-items:center;justify-content:center}

.section-title{font-size:30px;font-weight:800;letter-spacing:3px;color:var(--ink);text-transform:uppercase;text-align:center}
.section-lead{text-align:center;font-size:15px;line-height:26px;color:var(--text)}

/* how it works */
.how{position:absolute;top:665px;left:0;width:1200px;height:555px}
.how .section-title{margin-top:80px}
.how .section-lead{margin-top:26px}
.steps{position:absolute;top:210px;left:90px;width:1020px;display:flex}
.step{width:255px;text-align:center}
.step svg{height:110px}
.step h4{margin-top:38px;font-size:15px;font-weight:700;color:var(--ink);letter-spacing:1px;text-transform:uppercase}
.step p{margin:18px auto 0;width:200px;font-size:12.5px;line-height:22px}

/* about band */
.about{position:absolute;top:1220px;left:0;width:1200px;height:458px;background:linear-gradient(180deg,#3a4a4a 0%,#4c5f55 35%,#3b5a2e 70%,#2c4420 100%);text-align:center;color:var(--white)}
.about h2{margin-top:112px;font-size:30px;font-weight:800;letter-spacing:3px}
.about p{margin:30px auto 0;width:780px;font-size:14px;line-height:28px}
.about .btn{margin-top:34px}

/* teas */
.teas{position:absolute;top:1678px;left:0;width:1200px;height:867px}
.teas .section-title{margin-top:70px}
.teas .section-lead{margin-top:24px}
.products{position:absolute;top:243px;left:100px;width:1000px;display:flex;justify-content:space-between}
.product{width:300px;text-align:center}
.product-photo{width:300px;height:240px;background:radial-gradient(ellipse at 50% 45%,#6b3a22 0%,#4a2a1a 30%,#c9bfb3 60%,#ffffff 80%)}
.product h3{margin-top:62px;font-size:18px;font-weight:700;letter-spacing:1px;color:var(--ink);text-transform:uppercase}
.product .kind{margin-top:6px;font-size:16px;color:var(--text)}
.product .rule{width:56px;height:2px;background:var(--gold);margin:16px auto 0}
.product .desc{margin:20px auto 0;width:250px;font-size:12.5px;line-height:22px}
.product .price{margin-top:20px;font-size:25px;color:var(--price)}
.product .btn{margin-top:20px;padding:14px 32px}

/* advantages */
.advantages{position:absolute;top:2545px;left:0;width:1200px;height:600px;background:linear-gradient(135deg,#2c8c8c 0%,#3e9a95 40%,#2b7d80 70%,#23686c 100%);color:var(--white);text-align:center}
.advantages h2{margin-top:80px;font-size:30px;font-weight:800;letter-spacing:3px}
.advantages .lead{margin-top:22px;font-size:14px}
.adv-list{position:absolute;top:225px;left:90px;width:1020px;display:flex}
.adv{width:255px}
.adv svg{height:100px}
.adv h4{margin-top:40px;font-size:15px;font-weight:700;letter-spacing:1px;text-transform:uppercase}
.adv p{margin:18px auto 0;width:215px;font-size:12.5px;line-height:24px}

/* contact */
.contact{position:absolute;top:3145px;left:0;width:1200px;height:655px}
.contact .section-title{margin-top:80px}
.contact .section-lead{margin-top:26px}
.contact-info{position:absolute;top:255px;left:185px;width:245px;font-size:12.5px;line-height:22px}
.contact-info .intro{color:var(--ink);font-size:13px}
.contact-info .note{margin-top:14px;font-size:11.5px}
.contact-info h4{margin-top:26px;font-size:14px;font-weight:700;color:var(--ink);letter-spacing:1px;text-transform:uppercase}
.contact-info .details{margin-top:10px;font-size:11.5px}
.socials{margin-top:30px;display:flex;gap:8px}
.socials span{width:26px;height:26px;border-radius:50%;background:#6d7176}
.contact-form{position:absolute;top:255px;left:580px;width:450px}
.contact-form h4{font-size:13px;font-weight:700;color:var(--ink);letter-spacing:1px;text-transform:uppercase}
.field{margin-top:18px;border:1px solid var(--line);height:50px;padding:14px 16px;font-size:12.5px;color:var(--muted)}
.field.message{height:82px}
.contact-form .btn{margin-top:22px;padding:15px 38px}

/* footer */
.footer{position:absolute;top:3800px;left:0;width:1200px;height:291px;background:var(--footer);color:var(--footer-text);font-size:11.5px}
.footer-cols{position:absolute;top:52px;left:108px;display:flex;gap:0}
.footer-col{width:155px;line-height:28px}
.connect{position:absolute;top:46px;left:760px;width:345px}
.connect h4{color:var(--white);font-size:19px;font-weight:700;letter-spacing:.5px;text-transform:uppercase}
.subscribe{margin-top:18px;display:flex}
.subscribe .input{width:240px;height:40px;background:#3a3b40;padding:11px 14px;color:var(--footer-text)}
.subscribe .btn{padding:11px 22px;border-radius:0;font-size:13px}
.connect .line{margin-top:18px;display:flex;align-items:center;gap:10px}
.connect .line + .line{margin-top:10px}
.copyright{position:absolute;bottom:14px;left:0;width:1200px;text-align:center;font-size:10.5px;color:#85888d}
</style>
</head>
<body>

<header class="header">
  <div class="brand"><span class="brand-dot"></span><span class="brand-name">Leaf Hollow</span></div>
  <div class="utility">
    <span>My Account</span><span>My Cart</span><span>Login</span><span>Register</span>
    <span class="cart"><span class="cart-icon"><svg width="16" height="16" viewBox="0 0 16 16"><path d="M1 2h2l2 8h8l2-6H4" fill="none" stroke="#fff" stroke-width="1.5"/><circle cx="6" cy="13" r="1.3" fill="#fff"/><circle cx="12" cy="13" r="1.3" fill="#fff"/></svg></span>Your cart is: 0 items</span>
  </div>
  <nav class="nav"><span>Shop</span><span>Darjeeling</span><span>Pure &amp; Organic</span><span>About us</span><span>Advantages</span><span>How it works</span><span>Contact us</span></nav>
</header>

<section class="hero" role="img" aria-label="Photograph of a glass cup of amber Darjeeling tea beside a cast iron teapot and loose leaves">
  <h1>LEAF HOLLOW</h1>
  <p>We are an online retailer of organic Darjeeling tea</p>
  <span class="btn-outline">Order now!</span>
  <span class="scroll-down"><svg width="22" height="14" viewBox="0 0 22 14"><path d="M2 3l9 8 9-8" fill="none" stroke="#555" stroke-width="2"/></svg></span>
</section>

<section class="how">
  <h2 class="section-title">How it works</h2>
  <p class="section-lead">How can it be that we offer you one of the world's most sought after teas for an unbeatable low price?</p>
  <div class="steps">
    <div class="step">
      <svg viewBox="0 0 110 110" width="110"><g fill="none" stroke="var(--teal)" stroke-width="3" stroke-linejoin="round"><path d="M15 40l40-18 40 18-40 18z"/><path d="M15 40v40l40 18 40-18V40"/><path d="M55 58v40"/><path d="M15 40L4 55l40 18 11-15M95 40l11 15-40 18-11-15"/></g></svg>
      <h4>Large packages</h4>
      <p>By using large packets (500g, 1000g), we can save on packaging, labelling and handling costs.</p>
    </div>
    <div class="step">
      <svg viewBox="0 0 110 110" width="110"><g fill="none" stroke="var(--teal)" stroke-width="3"><rect x="30" y="10" width="50" height="92"/><path d="M30 18h50"/><path d="M40 30h8M62 30h8M40 46h8M62 46h8M40 62h8M62 62h8M40 78h8M62 78h8"/><path d="M48 102V88h14v14"/></g></svg>
      <h4>Direct trade</h4>
      <p>We cut all middlemen and buy directly from the leaf hollow in Darjeeling.</p>
    </div>
    <div class="step">
      <svg viewBox="0 0 110 110" width="110"><g fill="none" stroke="var(--teal)" stroke-width="3" stroke-linejoin="round"><path d="M60 10h38v38L50 96 12 58z"/><circle cx="82" cy="26" r="6"/><path d="M62 42c-6-6-18 0-12 8s-4 16-12 10M46 36l26 26"/></g></svg>
      <h4>Simplicity</h4>
      <p>We only sell 100% organic high grade FTGFOP-1 darjeeling tea to reduce costs. Nothing else.</p>
    </div>
    <div class="step">
      <svg viewBox="0 0 110 110" width="110"><g fill="none" stroke="var(--teal)" stroke-width="3" stroke-linejoin="round"><rect x="8" y="30" width="60" height="52"/><path d="M68 46h22l14 18v18H68"/><circle cx="28" cy="86" r="8" fill="#fff"/><circle cx="86" cy="86" r="8" fill="#fff"/><path d="M76 50v14h22"/></g></svg>
      <h4>One year's supply</h4>
      <p>We cut all middlemen and buy directly from the leaf hollow in Darjeeling.</p>
    </div>
  </div>
</section>

<section class="about" role="img" aria-label="Photograph of green tea plantation terraces under misty hills">
  <h2>ABOUT DARJEELING TEAS</h2>
  <p>We focus on only one sort of tea: the best. This helps us to set up a very simple supply chain that reduces storage and freight costs. By ordering tea in bulk directly from the tea plantation in India all unnecessary intermediaries that would increase handling costs are eliminated. Our big packages that go without costly design help to reduce packaging and labelling costs.</p>
  <span class="btn">Click here</span>
</section>

<section class="teas">
  <h2 class="section-title">Our Darjeeling teas</h2>
  <p class="section-lead">Looking for the world's most renowned tea at unbeatable low prices?<br>Available for limited time only.</p>
  <div class="products">
    <div class="product">
      <div class="product-photo" role="img" aria-label="Photograph of a brown cup of tea with loose black tea leaves"></div>
      <h3>First Flush 2016</h3>
      <p class="kind">Black, Organic Darjeeling Tea</p>
      <div class="rule"></div>
      <p class="desc">Our most popular Darjeeling Tea. An organic First Flush from the 2016 harvest with the highest gradation: FTGFOP-1.</p>
      <p class="price">£19.99 (for 500g)</p>
      <span class="btn">Order now</span>
    </div>
    <div class="product">
      <div class="product-photo" role="img" aria-label="Photograph of a brown cup of tea with loose black tea leaves"></div>
      <h3>Second Flush 2016</h3>
      <p class="kind">Black, Organic Darjeeling Tea</p>
      <div class="rule"></div>
      <p class="desc">A Second Flush from 2016 with the highest leaf grade: FTGFOP-1. From 100% organic cultivation, certified by the Green Soil Board.</p>
      <p class="price">£19.99 (for 500g)</p>
      <span class="btn">Order now</span>
    </div>
    <div class="product">
      <div class="product-photo" role="img" aria-label="Photograph of a brown cup of tea with loose green tea leaves"></div>
      <h3>Green Tea</h3>
      <p class="kind">Organic Darjeeling Tea</p>
      <div class="rule"></div>
      <p class="desc">Try our new Green Darjeeling Tea. An organic First Flush from the 2016 harvest with the highest gradation: FTGFOP-1.</p>
      <p class="price">£14.99 (for 500g)</p>
      <span class="btn">Order now</span>
    </div>
  </div>
</section>

<section class="advantages">
  <h2>ADVANTAGES</h2>
  <p class="lead">Your main benefits if you order at Leaf Hollow</p>
  <div class="adv-list">
    <div class="adv">
      <svg viewBox="0 0 100 100" width="100"><g fill="none" stroke="#fff" stroke-width="3"><path d="M14 10h72v44c0 20-18 32-36 40C32 86 14 74 14 54z"/><path d="M30 30l40 40M70 30L30 70"/></g></svg>
      <h4>Highest quality</h4>
      <p>We ensure you get First and Second Flush Teas with the highest leaf gradation: FTGFOP-1. Tasted by one of UK's most renowned tea tasters.</p>
    </div>
    <div class="adv">
      <svg viewBox="0 0 100 100" width="100"><g fill="none" stroke="#fff" stroke-width="3" stroke-linejoin="round"><path d="M40 96V20"/><path d="M40 24c8-10 18-12 24-10-2 8-10 16-24 18z"/><path d="M40 48c10-10 22-12 30-10-4 10-14 16-30 18z"/><path d="M40 70c10-8 20-10 28-8-4 8-12 14-28 16z"/></g></svg>
      <h4>100% Organic</h4>
      <p>All our tea is from certified organic production, inspected by internationally reputable service providers.</p>
    </div>
    <div class="adv">
      <svg viewBox="0 0 100 100" width="100"><g fill="none" stroke="#fff" stroke-width="3"><circle cx="40" cy="40" r="26"/><path d="M59 59l30 30"/></g></svg>
      <h4>Full transparency</h4>
      <p>Look up pesticide analysis results of your tea and find out from which Darjeeling tea estate your tea came from by using the batch number of your tea package.</p>
    </div>
    <div class="adv">
      <svg viewBox="0 0 100 100" width="100"><g fill="none" stroke="#fff" stroke-width="3" stroke-linejoin="round"><path d="M52 8h38v38L46 90 8 52z"/><circle cx="74" cy="24" r="6"/><path d="M56 40c-6-6-16 0-11 7s-4 14-11 9M42 34l22 22"/></g></svg>
      <h4>Low price</h4>
      <p>We did everything to eliminate all unnecessary costs in order to provide you the lowest possible price.</p>
    </div>
  </div>
</section>

<section class="contact">
  <h2 class="section-title">Contact us</h2>
  <p class="section-lead">Do you still have any questions?<br>One way to get in touch with us is to fill out the following form.</p>
  <div class="contact-info">
    <p class="intro">If you are contacting us for a business proposal or regarding advertising please mention it in your message.</p>
    <p class="note">Please provide as much information as you can, one of us will be in touch with you soon. Further information can also be found on our FAQ page.</p>
    <h4>Verdane Organics</h4>
    <p class="details">Phone: +1 123 456 789<br>Email: info@leafhollow.co.uk</p>
    <div class="socials"><span></span><span></span><span></span><span></span><span></span><span></span></div>
  </div>
  <div class="contact-form">
    <h4>Contact form</h4>
    <div class="field">Name</div>
    <div class="field">Email</div>
    <div class="field message">Message</div>
    <span class="btn">Send message</span>
  </div>
</section>

<footer class="footer">
  <div class="footer-cols">
    <div class="footer-col">Shop<br>Darjeeling<br>Pure &amp; Organic<br>Advantages<br>How it works</div>
    <div class="footer-col">Login<br>About Us<br>Service Area<br>Contact Us</div>
    <div class="footer-col">Book Now<br>Buy Gift Cards<br>Charity<br>Help Page</div>
    <div class="footer-col">Spread The Love<br>Privacy Policy<br>Terms of Conditions<br>Sitemap</div>
  </div>
  <div class="connect">
    <h4>Stay connected</h4>
    <div class="subscribe"><span class="input">Enter your email id</span><span class="btn">Signup</span></div>
    <div class="line"><svg width="12" height="12" viewBox="0 0 12 12"><path d="M2 1h3l1 3-2 1c1 2 2 3 4 4l1-2 3 1v3c-6 0-10-4-10-10z" fill="var(--teal-light)"/></svg>Phone: +1 123 456 789</div>
    <div class="line"><svg width="12" height="10" viewBox="0 0 12 10"><rect x="0.5" y="0.5" width="11" height="9" fill="none" stroke="var(--teal-light)"/><path d="M1 1l5 4 5-4" fill="none" stroke="var(--teal-light)"/></svg>Email: info@leafhollow.co.uk</div>
  </div>
  <p class="copyright">Copyright © 2016, Leaf Hollow. All rights reserved.</p>
</footer>

</body>
</html>
```